Webdesign für Seminaranbieter
Zielgruppe
Die Velunor Academy bietet Kurse, Seminare & Coachings im Bereich der Kommunikation / Persönlichkeitsentwicklung an.
Folgendes Angebot besteht zur Zeit:
Seminare:
- 'Brückenbau Grundkurs Praxis', eine Einführung in die Kommunikation.
- 'Starke Wurzeln, offene Herzen' zum Thema Erziehung.
- 'Reife Jahre mit Gelassenheit', zum Thema Älter werden und den Umgang damit.
Kurse:
- 'Gewaltfreie Kommunikation', Übungsgruppe
Coaching:
- Einzelsitzungen mit Hypnose
Ps: im Anhang unter 'Angabot_Vorlage.pdf' finden Sie mehr Infos zu den einezlenen Angebote.
Aufgabenstellung
Bitte berücksichtigen Sie, dass bereits ein Logo besteht (siehe Anhang).
Vom gesamteindruck her sollte die Website aufgeräumt, übersichtlich, harmonisch, freundlich & frisch wirken.
Es wäre super, wenn die Website authentisch wirkt (und weniger '0815 Business Website').
Bitte bedenken Sie, dass die Website sich an Private richtet, die sich nach einem 'strahlenderen & unbeschwerterem Lebene sehnen'.
Wir haben bereits viele Persönlichkeiten stärken können und möchten dies auch witerhin mit viel Herzblut machen.

```html
<!DOCTYPE html>
<html lang="de">
<head>
<meta charset="utf-8">
<title>Velunor Academy – Neue Perspectiven · Neue Horizonte</title>
<link href="https://fonts.googleapis.com/css2?family=Raleway:ital,wght@0,400;0,500;0,600;0,700;1,400&display=swap" rel="stylesheet">
<style>
:root{
  --bg-outer:#ede6e0;
  --bg-edge:#f8f5f2;
  --page:#ffffff;
  --panel:#f3f0eb;
  --plum:#5e5068;
  --ink:#3d3a3a;
  --text:#555050;
  --accent:#f26c44;
  --peach:#efb57e;
  --taupe:#9a8574;
  --line:#9d9a98;
}
*{box-sizing:border-box;margin:0;padding:0}
html,body{width:1200px;height:3034px;overflow:hidden}
body{background:var(--bg-outer);font-family:'Raleway',sans-serif;color:var(--text);position:relative}
.edge{position:absolute;left:0;top:0;width:73px;height:3034px;background:var(--bg-edge)}
.page{position:absolute;left:203px;top:56px;width:908px;height:2925px;background:var(--page)}
.abs{position:absolute}

/* hero */
.hero{left:0;top:0;width:908px;height:530px;background:linear-gradient(120deg,#e9d2bd 0%,#caa386 35%,#d9bba3 60%,#f1e3d3 100%)}
.topbar{left:0;top:0;width:908px;height:56px;background:rgba(255,255,255,.55)}
.brand{left:28px;top:19px;font-weight:600;font-size:12px;letter-spacing:2px;color:var(--ink)}
.nav{right:46px;top:22px;display:flex;gap:28px;font-size:12px;font-weight:500;color:#222;letter-spacing:.5px}
.nav span.active{color:var(--accent);border:1.5px solid var(--accent);border-radius:2px;padding:2px 10px;margin-top:-4px}
.hero-title{left:0;width:908px;top:374px;text-align:center;color:#fff;font-size:38px;letter-spacing:4px;font-weight:500}
.hero-sub{left:0;width:908px;top:433px;text-align:center;color:#fff;font-size:19px;letter-spacing:1.5px;font-weight:600}
.arrow{top:248px}
.dots{left:433px;top:504px;display:flex;gap:5px}
.dots i{width:7px;height:7px;border-radius:50%;border:1px solid #fff;display:block}
.dots i.on{background:#fff}

/* newsletter */
.newsletter{left:0;top:544px;width:908px;height:61px;background:var(--peach)}
.nl-label{left:135px;top:26px;color:#fff;font-size:10.5px;font-weight:600;letter-spacing:.3px}
.nl-field{left:397px;top:14px;width:320px;height:30px;background:#fff;border:1px solid #d8cfc6;font-size:10.5px;letter-spacing:1px;color:#888;padding:9px 10px}
.nl-ok{left:731px;top:17px;width:37px;height:22px;background:var(--accent);color:#fff;font-size:11px;font-weight:600;text-align:center;line-height:22px;letter-spacing:1px}

/* intro */
.intro-title{left:0;width:908px;top:656px;text-align:center;font-size:26px;letter-spacing:1px;color:var(--plum);font-weight:500}
.intro-box{left:134px;top:705px;width:676px;height:193px;background:var(--panel);padding:26px 50px;font-size:13.4px;line-height:13px;color:#444}
.intro-box p{margin-bottom:13px}

/* offers banner */
.offers-banner{left:0;top:982px;width:908px;height:175px;background:linear-gradient(180deg,#f4e8d6 0%,#f7e2c3 55%,#efc99a 100%)}
.offers-title{left:0;width:908px;top:1060px;text-align:center;font-size:26px;letter-spacing:1px;color:var(--plum);font-weight:500;padding-left:26px}

/* cards */
.card{left:64px;width:780px;height:190px;background:var(--panel)}
.card .thumb{position:absolute;left:69px;top:20px;width:156px;height:135px}
.card .body{position:absolute;left:262px;top:20px;width:483px}
.card h3{font-size:13px;font-weight:700;color:var(--plum);letter-spacing:.3px;margin-bottom:14px}
.card p{font-size:9.3px;line-height:12.6px;color:#4a4a4a;text-align:justify;margin-bottom:12px}
.card em{font-style:italic}
.more{position:absolute;left:262px;top:156px;width:60px;height:20px;background:var(--accent);color:#fff;font-size:7.5px;font-weight:700;letter-spacing:1px;text-align:center;line-height:20px}

/* photo band */
.photo-band{left:0;top:2257px;width:908px;height:253px;background:linear-gradient(180deg,#bdb3ad 0%,#d8cdc3 45%,#8e8682 75%,#4a403b 100%)}

/* footer */
.f-name{left:60px;top:2630px;width:275px;text-align:center;font-size:15px;letter-spacing:2.5px;color:var(--ink);font-weight:500}
.f-info{left:60px;top:2683px;width:275px;text-align:center;font-size:13px;color:#555;line-height:16px}
.f-info b{display:block;font-weight:600;margin-bottom:16px;letter-spacing:.5px}
.f-info .gap{display:block;height:14px}
.f-q{left:474px;top:2541px;font-size:13px;letter-spacing:.8px;color:#444;line-height:15px;font-weight:500}
.field{left:474px;width:320px;border:1.5px solid #a19d9b;background:#fff;font-size:10.5px;letter-spacing:1px;color:#888;padding:9px 15px}
.send{left:476px;top:2786px;width:165px;height:32px;background:var(--accent);color:#fff;font-size:11px;font-weight:600;letter-spacing:1.5px;text-align:center;line-height:32px}

.bottom-bar{left:0;top:2849px;width:908px;height:76px;background:var(--taupe);color:#fff;font-size:13px;letter-spacing:.5px}
.bottom-bar span{position:absolute;top:30px}
</style>
</head>
<body>
<div class="edge"></div>
<main class="page">

  <section class="abs hero" role="img" aria-label="Foto einer lachenden Familie, die gemeinsam ein Buch liest, in warmem Licht"></section>
  <header class="abs topbar">
    <div class="abs brand">VELUNOR ACADEMY</div>
    <nav class="abs nav"><span class="active">HOME</span><span>ANGEBOT</span><span>KONTAKT</span><span>ÜBER UNS</span></nav>
  </header>
  <svg class="abs arrow" style="left:20px" width="26" height="44" viewBox="0 0 26 44"><polyline points="22,3 4,22 22,41" fill="none" stroke="#fff" stroke-width="2"/></svg>
  <svg class="abs arrow" style="left:862px" width="26" height="44" viewBox="0 0 26 44"><polyline points="4,3 22,22 4,41" fill="none" stroke="#fff" stroke-width="2"/></svg>
  <h1 class="abs hero-title">VELUNOR ACADEMY</h1>
  <p class="abs hero-sub">NEUE PERSPECTIVEN · NEUE HORIZONTE</p>
  <div class="abs dots"><i class="on"></i><i></i><i></i></div>

  <section class="abs newsletter">
    <span class="abs nl-label">ABONNIEREN SIE UNSEREN NEWSLETTER!</span>
    <div class="abs nl-field">E-MAIL ADRESSE</div>
    <div class="abs nl-ok">OK</div>
  </section>

  <h2 class="abs intro-title">CHANCE AUF EIN NEUES LEVEL ZU KOMMEN</h2>
  <div class="abs intro-box">
    <p>Lorem ipsum dolor sit amet, mea cu nihil torquatos. Ad error civibus vivendum nec. Antiopam praesent sea an, id nam alii facete elaboraret.</p>
    <p>Urbanitas adolescens vituperatoribus vel in. Lorem voluptua posidonium eu sea, esse fabellas cu eam, cu vim tation nusquam. Nostrum iudicabit vix et, tota vivendo nominati has cu.</p>
    <p>Lorem ipsum dolor sit amet, mea cu nihil torquatos. Ad error civibus vivendum nec. Antiopam praesent sea an, id nam alii facete elaboraret. Urbanitas adolescens vituperatoribus vel in. Lorem voluptua posidonium eu sea, esse fabellas cu eam.</p>
  </div>

  <section class="abs offers-banner" role="img" aria-label="Foto eines Leuchtturms vor hellem Abendhimmel"></section>
  <h2 class="abs offers-title">UNSERE AKTUELLE ANGEBOTE</h2>

  <article class="abs card" style="top:1188px">
    <div class="thumb" role="img" aria-label="Foto gestapelter Steine am Strand" style="background:linear-gradient(160deg,#e9e2da,#c9a27a 55%,#8f7f73)"></div>
    <div class="body">
      <h3>SEMINAR: Brückenbau Grundkurs Praxis</h3>
      <p>Jedes zusammenleben erfordert Kommunikation; ob in der Familie (auch mit Kindern), im Freundeskreis, oder im Arbeitsalltag. Verstehen und verstanden werden sind ausschlaggebend für Effektivität am Arbeitsplatz sowie Harmonie und erfüllende Beziehungen im persönlichen Leben.</p>
      <p>Sich selber besser zu verstehen eröffnet ungeahnte Möglichkeiten und Wahlfreiheit.</p>
    </div>
    <div class="more">MEHR</div>
  </article>

  <article class="abs card" style="top:1393px">
    <div class="thumb" role="img" aria-label="Schwarzweißfoto einer Familie beim Spaziergang auf einer Brücke" style="background:linear-gradient(160deg,#b9b6b3,#7c7876 60%,#9a9693)"></div>
    <div class="body">
      <h3>SEMINAR: Starke Wurzeln, offene Herzen</h3>
      <p><em>„Unter Erziehung versteht man die pädagogische Einflussnahme auf die Entwicklung und das Verhalten Heranwachsender“.</em> Erziehungstheorien gibt es unzählige, die das Spektrum von streng und autoritär bis hin zum Laisser-faire decken. Das selbst erlebte wird z.T. auch unreflektiert wiederholt und/oder wir verlieren uns in unzählige Ratgeber.</p>
      <p>Mithilfe der Neurowissenschaften wird uns klar, dass das oft kräftezerrende Ringen rund um die Erziehung absolut unnötig und überflüssig ist, ja sogar schädigend.</p>
    </div>
    <div class="more">MEHR</div>
  </article>

  <article class="abs card" style="top:1597px">
    <div class="thumb" role="img" aria-label="Nahaufnahme eines Uhrenziffernblatts" style="background:linear-gradient(140deg,#5f5a58,#d9d4d0 50%,#8a8583)"></div>
    <div class="body">
      <h3>SEMINAR: Zeit und Alternativen</h3>
      <p>Zeit ist ein allgegenwärtiges (und manchmal leidiges) Thema, wie z.B „keine Zeit haben“ oder „die Zeit verfliegt im Nu“. Was IST jedoch Zeit? Wie und wo nehmen wir sie wahr? Welche Auswirkungen hat das „Zeit denken“? Was wäre, wenn wir der Zeit entkommen – aussteigen – könnten? Mit welchen Folgen? Welchen Zusammenhang haben Zeit und Alter?</p>
      <p><em>„Älter werden ist unumgänglich. Alt werden ist optional.“</em></p>
    </div>
    <div class="more">MEHR</div>
  </article>

  <article class="abs card" style="top:1804px">
    <div class="thumb" role="img" aria-label="Foto von Gräsern vor Bergen im Gegenlicht" style="background:linear-gradient(180deg,#cfd6d8,#e3cfb0 50%,#a88a5e)"></div>
    <div class="body">
      <h3>SEMINAR: Gibt es Auswege aus DER Realität?</h3>
      <p>Willkommen in der Realität!<br>Wir reden von DER Realität, der wir uns realistischer Weise beugen müssen. Was ist jedoch Realität? Wirk-lichkeit – etwas das „wirkt“? Tatsachen – wahrnehmbare Vorgänge? Wenn sie das ist, was wir wahrnehmen, ist sie subjektiv und liegt im Auge des Betrachters?<br>Wie bildet sich die Realität die wir erleben? Können wir Einfluss darauf nehmen?</p>
      <p>Könnten wir sie gar ändern?</p>
    </div>
    <div class="more">MEHR</div>
  </article>

  <article class="abs card" style="top:2013px">
    <div class="thumb" role="img" aria-label="Foto einer Wendeltreppe von oben" style="background:radial-gradient(circle at 60% 70%,#3f3c3b,#9c9896 45%,#d4d0cc)"></div>
    <div class="body">
      <h3>EINZELSITZUNGEN: Coaching mit Hypnose</h3>
      <p>Einzelsitzungen...</p>
      <p>Hast du Lust, die Kraft deines Unterbewusstseins zu erfahren?<br>Hypnose macht es erlebbar und ermöglicht, Veränderungsarbeit (wie z.B. Verhalten, Rauchen, Phobien...) erfolgreich umzusetzen</p>
    </div>
    <div class="more">MEHR</div>
  </article>

  <section class="abs photo-band" role="img" aria-label="Foto einer Person, die bei Sonnenuntergang auf einem Felsen über einem Tal sitzt"></section>

  <footer>
    <div class="abs f-name">VELUNOR ACADEMY</div>
    <div class="abs f-info">
      <b>VELUNOR ACADEMY GMBH.</b>
      Lindenweg 17<br>4312 Talberg
      <span class="gap"></span>
      TEL: 0176 482 915<br>info@velunoracademy.ch
    </div>

    <div class="abs f-q">NOCH FRAGEN, ANREGUNGEN?<br>SCHREIBEN SIE UNS!</div>
    <div class="abs field" style="top:2588px;height:32px">NAME</div>
    <div class="abs field" style="top:2632px;height:31px">E-MAIL ADRESSE</div>
    <div class="abs field" style="top:2673px;height:99px">NACHRICHT</div>
    <div class="abs send">SENDEN</div>

    <div class="abs bottom-bar">
      <span style="left:55px">Datenschutz</span>
      <span style="left:172px">Impressum</span>
      <span style="left:386px">VELUNOR ACADEMY | 2019</span>
    </div>
  </footer>
</main>
</body>
</html>
```